FOOD PACKAGING DESIGN FOR 3REE CEDAR PANTRY - BRIEF UPDATED..

Hello Everyone

After discussions with Artisan Hive and the amount of work on this project, we have decided to split this project into phase 1 and phase 2 to make it more fair.

The allocated design budget is for Phase 1 only but we have included phase 2 below so you see the long term vision on this.

Phase 1 are products which we would like immediate designs on, once a winner is selected we will agree a fee with the designer via artisan hive and design phase 2 products too.

This will ensure a reasonable number of designs for each phase.

After the successful design of a logo on artisan hive, this is a packaging design project for Cedarfield Pantry‎.

Initially this is not guaranteed as on a couple of occasions in the past we have been disappointed with the response but as soon as we receive a couple of designs that we believe we can take live, IMMEDIATELY WE WILL PAYMENT GUARANTEE THIS PROJECT, WITHOUT ANY HESITATION AND THIS IS NOT OUR FIRST PROJECT ON ARTISAN HIVE, PAYMENT HAS ALREADY BEEN MADE TO ARTISAN HIVE, IT IS JUST A MATTER OF RECEIVING SOME GOOD DESIGNS NOW AND WE’LL GUARANTEE IT.

This will be a big design project so we only want designers that can work with us on this long term.

We are a frozen food manufacturer and wholesaler and we are now looking to launch a retail brand under the name Cedarfield Pantry, you can find more information about our company and what we sell by visiting our main website www.norvelchill.com .

All the packaging we design will be for frozen food packaging.

The packaging will be frozen food bags and also folding carton boxes.

PHASE 1 BAGS:

Samosas:

1. 10, 20 and 50 Pack Meat ‎Samosas – One design but 3 pack sizes for all.
2. 10, 20 and 50 Pack Chicken Samosas
3. 10, 20 and 50 Pack Vegetable Samosas
4. 10, 20 and 50 Pack Chicken Tikka Samosas

Spring Rolls:

5. 10, 20 and 50 Pack Meat Spring Rolls – Again, one design but 3 pack sizes.
6. 10, 20 and 50 Pack Chicken Spring Rolls
7. 10, 20 and 50 Pack Vegetable Spring Rolls
8. 10, 20 and 50 Pack Chicken Tikka Spring Rolls

Seekh Kebabs:

9. 10 and 20 Pack Meat Seekh Kebabs – Ready Cooked (small writing not heading).
10. 10 and 20 Pack Chicken Seekh Kebabs – Ready Cooked (small writing not heading).

Chapli Kebabs:

11. Meat Chapli Kebabs, 8 Pack (500g) – Ready Cooked (small writing not heading).
12. Chicken Chapli Kebabs, 8 Pack (500g) – Ready Cooked (small writing not heading).

Doners and Shawarma Kebabs:

13. Cooked, Sliced, Traditional Doner Kebab – 1kg

Sausages:

14. 10 and 20 Pack Lamb Sausages
15. 10 and 20 Pack Beef Sausages
16. 10 and 20 Pack Chicken Sausages

Coated Chicken Range:

17. 750g and 1kg Battered Chicken Nuggets
18. 750g and 1kg‎ Breaded Chicken Nuggets

19. 750g and 1kg Battered Chicken Pops
20. 750g and 1kg‎ Breaded Chicken Pops

21. 750g and 1kg Battered Chicken Goujon Strips

22. 750g and 1kg‎ Breaded Chicken Goujon Strips

23. 10 Battered Chicken Burgers – Approx 850g
24. 10 Breaded Chicken Burgers – Approx 850g
25. 10 Southern Fried Chicken Burgers – Approx 850g

26. 1kg Battered Chicken Wings
27. 1kg Breaded Chicken Wings

BOXES – FOLDING CARTONS – PHASE 1:

Boxes will be as follows:

Burgers:

1. 8 Pack - Beef Burgers
2. 8 Pack - Chicken Burgers
3. 8 Pack - Lamb Burgers

PHASE 2 BAGS:

Shami Kebabs:

1. Meat Shami Kebabs, 8 Pack (500g) – Ready Cooked (small writing not heading).
2. Chicken Shami Kebabs‎, 8 Pack (500g) – Ready Cooked (small writing not heading).

1. Cooked, Sliced, Plain Chicken Shawarma – 1 kg
2. Cooked, Sliced, Tandoori Chicken Shawarma – 1 kg
3. Cooked, Sliced, Chicken Tikka Shawarma – 1 kg

Chicken Wings:

1. 1kg Hot & Spicy Chicken Wings
2. 1kg BBQ Chicken Wings
3. 1kg Peri Peri Chicken Wings
4. 1kg Tandoori Chicken Wings

At this stage we are looking for the design ideas and we’ll confirm the exact bag size when we select the final winner, here are some size guidelines:

• 10 Pack Bag Size – Length 23cm x Width 23cm
• 20 Pack Bag Size – Length 29cm x Width 24cm
• 50 Pack Bag Size – Length 34cm x Width 31cm
• 500g Bag Size – Length 27cm x Width 24cm
• 750g Bag Size – Length 29cm x Width 24cm
• 1kg Bag Size – Length 31cm x Width 27cm

BOXES – FOLDING CARTONS – PHASE 2:

Boxes will be as follows:

Seekh Kebabs:

1. 10 Pack and 20 Pack Lamb Seekh Kebabs – Ready Cooked (small writing not heading).

2. 10 Pack and 20 Pack Chicken Seekh Kebabs – Ready Cooked (small writing not heading).

Sausages:

3. 10 Pack Lamb Sausages
4. 10 Pack Beef Sausages
5. 10 Pack Chicken Sausages

6. 10 Pack Lamb Sausage Rolls
7. 10 Pack Beef Sausage Rolls
8. 10 Pack Chicken Sausage Rolls

Pies:

9. Chicken & Mushroom Pie – 12cm Length x 12cm Width x 4cm Depth
10. Chicken Tikka Pie – 12cm Length x 12cm Width x 5cm Depth
11. Steak & Kidney Pie – 12cm Length x 12cm Width x 4cm Depth
12. Meat & Onion Pie – 12cm Length x 12cm Width x 4cm Depth
13. Meat & Potato Pie – 12cm Length x 12cm Width x 5.5cm Depth

Pasties:

14. Chicken Tikka Pasty – 12cm Length x 12cm Width x 5cm Depth
15. Chicken & Sweetcorn Pasty – 12cm Length x 12cm Width x 5cm Depth
16. Keema Pasty – 12cm Length x 12cm Width x 5cm Depth

Ready Meals:

16cm Length x 16cm Width x 5cm

17. Lasagne
18. Chicken Curry & Rice
19. Chicken Tikka Masala & Rice
20. Butter Chicken & Rice
21. Chicken Jalfrezi & Rice
22. Chicken Saag & Rice
23. Lamb Curry & Rice
24. Lamb Rogan Josh & Rice
25. Daal Makhni & Rice
26. Mattar Paneer & Rice

Box Sizes:

• 10 Pack Box – Length 12cm x Width 25cm x Depth 5cm
• 20 Pack Box – To be Confirmed.
• Ready Meals - 16cm Length x 16cm Width x 5cm

The packaging that is designed must be clean and crisp with a classy premium feel to it, see the attached examples or email us for more ideas of what we like.

18. https://www.pinvault.example/pin/100000000000000001/
19. https://www.pinvault.example/pin/1000000000000002/
20. https://www.pinvault.example/pin/100000000000000003/
21. https://www.pinvault.example/pin/10000000000000004/
22. https://www.pinvault.example/pin/1000000000000005/
23. https://www.pinvault.example/pin/100000000000000006/
24. https://www.pinvault.example/pin/100000000000000007/
25. https://www.pinvault.example/pin/100000000000000008/
26. https://velmora.example/products/
27. http://www.packnotes.example/blog/2017/4/4/brisvale-creamery-updated-packaging-now-features-a-tapestry-of-flavor
28. https://www.pinvault.example/pin/100000000000000009/
29. https://www.pinvault.example/pin/100000000000000010/
30. https://www.folioyard.example/gallery/1000001/MEDICINE-PACKAGE
31. https://www.pinvault.example/pin/100000000000000011/
32. https://www.pinvault.example/pin/100000000000000012/
33. https://www.pinvault.example/pin/100000000000000013/
34. https://www.pinvault.example/pin/100000000000000014/

Our Competitors:

To help the designers, we have enclosed some links below of what our competitors are doing and how their packaging is designed, please note we don’t want anyone to copy their designs, ideas or styles, we are looking for something original but these links are given to help you so you can see what others are doing in our industry:

• http://toravelfare.example/products/ - Samosas, Spring Rolls, Kebabs etc, Bags
• http://www.zmb-eats.example/ - Burgers, Sausages, Kebabs etc, folding cartons.
• http://finemorsel.example/assets/product-catalogue-2016.pdf - all foods
• https://ochrelane.example/frozen-meals/ - ready meals

The packaging will have the following details on it:

1. Images of products for example sausages, burgers, chicken nuggets etc.

2. Quantity per pack - Front

3. Weight per pack – Front or Back.

4. Bar code – Back – to be provided for each item once winner is selected.

5. Halal logo at front‎.

6. Ingredients - Back

7. Possibly multilingual ingredients - Back, English, French, German etc.

8. Cooking instructions – Back.

9. Nutritional information table - Back.

10. Factory health mark of where the product is manufactured - Back

11. Contact details stating, "3ree Cedars is a Norvel Chill brand", followed by contact details, Tel: +44 (0) 800 013 4927, info@norvelchill.com, www.norvelchill.com, www.3reecedarpantry.com

We have attached some images of samosas, spring rolls, burgers, kebabs, pies and pasties etc to help with the design but you don’t have to use these images you can select your own at the initial stage, if we don’t like the image, we will provide these or we’ll select from picbarn, frame depot etc.

The winning Cedarfield Pantry Logo from Artisan Hive has been attached.

Norvel Chill (parent company logo) has also been attached so it can be used on the back of each packaging.

This will be an ongoing project where there will be regular work for the designer that is selected as the brand grows and we add more products to the brand.

Initially we are just looking for ideas on the packaging design but once finalised we would need it adjusted to the correct print size and resolution.

Thank you and we look forward to receiving your packaging ideas.

Norvel Chill

Target Market(s)

Food and drink industry, general public, halal market, Muslim customer base.

Industry/Entity Type

Crowd

Requirements
Must have
• Please read brief.
Nice to have
• Please read brief.

```html
<!DOCTYPE html>
<html lang="en">
<head>
<meta charset="utf-8">
<title>Cedarfield Pantry – Frozen Food Bags</title>
<link rel="stylesheet" href="https://fonts.googleapis.com/css2?family=Montserrat:wght@600;700&family=Oswald:wght@600&display=swap">
<style>
  :root{
    --page:#eeeff1;
    --bag-yellow:#f6c51c;
    --bag-yellow-light:#fbd94a;
    --bag-orange:#f29a14;
    --ink:#1d1d1b;
    --brand-blue:#1f3f96;
    --green:#2f8a3a;
    --blue:#1f3485;
    --purple:#6c1a68;
    --halal:#2e8a4a;
    --crimp:#d7d8da;
    --pack-text:#3a3a3a;
  }
  *{box-sizing:border-box;margin:0;padding:0}
  html,body{width:1200px;height:960px;overflow:hidden}
  body{
    background:var(--page);
    font-family:"Montserrat",Arial,sans-serif;
    color:var(--ink);
    position:relative;
  }
  .range{
    position:absolute;left:94px;top:238px;
    display:flex;gap:16px;
  }
  .bag{
    position:relative;width:326px;height:448px;overflow:hidden;
    background:
      linear-gradient(90deg,transparent 0 33%,rgba(255,255,255,.14) 33% 67%,transparent 67%),
      radial-gradient(ellipse at 0% 55%,var(--bag-orange) 0,rgba(242,154,20,0) 45%),
      linear-gradient(180deg,var(--bag-yellow-light),var(--bag-yellow));
  }
  .crimp{
    position:absolute;left:0;right:0;height:20px;
    background:repeating-linear-gradient(90deg,rgba(0,0,0,.06) 0 2px,transparent 2px 6px);
  }
  .crimp--top{top:0;background-color:var(--bag-yellow)}
  .crimp--bottom{bottom:0;height:26px;background-color:var(--crimp)}
  .brand{
    position:absolute;top:66px;left:0;right:0;text-align:center;
    font-weight:700;font-size:19px;line-height:24px;color:var(--brand-blue);
  }
  .claim{
    position:absolute;top:118px;left:0;right:0;text-align:center;
    font-weight:600;font-size:13.5px;line-height:16px;color:var(--ink);
  }
  .photo{
    position:absolute;left:0;right:0;top:226px;bottom:26px;
  }
  .photo--rolls{background:radial-gradient(ellipse at 42% 45%,#e3b572 0,#d9b27a 26%,#eef0f2 55%,#dcdee2 100%)}
  .photo--samosas{background:radial-gradient(ellipse at 48% 48%,#d7a15a 0,#cf9e62 30%,#e8e9ec 62%,#d4d6da 100%)}
  .photo--kebabs{background:radial-gradient(ellipse at 50% 45%,#9a5a3a 0,#8c4e33 40%,#b86f45 72%,#d9b58e 100%)}
  .banner{position:absolute;left:0;top:152px;width:326px;height:100px}
  .banner svg{display:block}
  .banner__text{
    position:absolute;left:40px;right:4px;top:24px;text-align:center;
    font-family:"Oswald",Impact,sans-serif;font-weight:600;
    font-size:28px;line-height:36px;color:#fff;white-space:nowrap;
    transform:rotate(-3deg) scaleX(.82);transform-origin:center;
  }
  .halal{
    position:absolute;left:238px;top:328px;width:68px;height:68px;border-radius:50%;
    background:var(--halal);border:3px solid #fff;
  }
  .pack{
    position:absolute;left:19px;top:390px;
    font-weight:700;font-size:13.5px;line-height:16px;color:var(--pack-text);
  }
</style>
</head>
<body>
<main class="range">

  <section class="bag">
    <div class="crimp crimp--top"></div>
    <div class="brand">Cedarfield Pantry</div>
    <p class="claim">100% ALL NATURAL<br>INGREDIENTS</p>
    <div class="photo photo--rolls" role="img" aria-label="Golden fried chicken spring rolls on a white plate with parsley"></div>
    <div class="banner">
      <svg width="326" height="100" viewBox="0 0 326 100">
        <path d="M10 30 Q170 4 326 8 L326 78 Q170 70 58 96 L52 64 Z" fill="#fff"/>
        <path d="M22 34 Q170 12 326 16 L326 70 Q170 62 62 86 L58 60 Z" fill="var(--green)"/>
      </svg>
      <div class="banner__text">CHICKEN SPRING ROLLS</div>
    </div>
    <div class="halal" aria-label="Halal certification mark"></div>
    <div class="pack">20 Pack</div>
    <div class="crimp crimp--bottom"></div>
  </section>

  <section class="bag">
    <div class="crimp crimp--top"></div>
    <div class="brand">Cedarfield Pantry</div>
    <p class="claim">100% ALL NATURAL<br>INGREDIENTS</p>
    <div class="photo photo--samosas" role="img" aria-label="Crisp triangular meat samosas, one cut open to show the filling"></div>
    <div class="banner">
      <svg width="326" height="100" viewBox="0 0 326 100">
        <path d="M10 30 Q170 4 326 8 L326 78 Q170 70 58 96 L52 64 Z" fill="#fff"/>
        <path d="M22 34 Q170 12 326 16 L326 70 Q170 62 62 86 L58 60 Z" fill="var(--blue)"/>
      </svg>
      <div class="banner__text">MEAT SAMOSAS</div>
    </div>
    <div class="halal" aria-label="Halal certification mark"></div>
    <div class="pack">20 Pack</div>
    <div class="crimp crimp--bottom"></div>
  </section>

  <section class="bag">
    <div class="crimp crimp--top"></div>
    <div class="brand">Cedarfield Pantry</div>
    <p class="claim">100% ALL NATURAL<br>INGREDIENTS</p>
    <div class="photo photo--kebabs" role="img" aria-label="Grilled meat chapli kebabs topped with tomato slices and green peppers"></div>
    <div class="banner">
      <svg width="326" height="100" viewBox="0 0 326 100">
        <path d="M10 30 Q170 4 326 8 L326 78 Q170 70 58 96 L52 64 Z" fill="#fff"/>
        <path d="M22 34 Q170 12 326 16 L326 70 Q170 62 62 86 L58 60 Z" fill="var(--purple)"/>
      </svg>
      <div class="banner__text">MEAT CHAPLI KEBABS</div>
    </div>
    <div class="halal" aria-label="Halal certification mark"></div>
    <div class="pack">8 Pack (500g)</div>
    <div class="crimp crimp--bottom"></div>
  </section>

</main>
</body>
</html>
```